Infographic Table of AI Pricing Options for LinkedIn post

Turn this table (in the powerpoint slide attached) into an attractively formatted infographic table for Strelquin (www.strelquin.com).
This will be an infographic displayed on a linkedin post from a consultant from Strelquin.
Try to keep it on brand with Strelquin look and feel.

Target Market(s)

Tech and SaaS CEOs and Founders; Private Equity and Venture Capital employees

Industry/Entity Type

Management Consulting

Colors
0054AA
0677BA
7BADD7
CADEEF
E8F1F8

```html
<!DOCTYPE html>
<html lang="en">
<head>
<meta charset="utf-8">
<title>Strelquin – Challenges of GenAI Monetization</title>
<link href="https://fonts.googleapis.com/css2?family=Outfit:wght@400;500;600;700;800&display=swap" rel="stylesheet">
<style>
  :root{
    --navy-deep:#0c0c34;
    --navy:#1a2160;
    --navy-light:#2b3a86;
    --brand-blue:#0054AA;
    --brand-mid:#0677BA;
    --brand-sky:#7BADD7;
    --brand-pale:#CADEEF;
    --brand-mist:#E8F1F8;
    --teal:#3fc0c6;
    --card:#f7f7fb;
    --ink:#16182c;
    --rule:#5a66a8;
    --pro:#1fae5a;
    --con:#e01616;
  }
  *{box-sizing:border-box;margin:0;padding:0}
  html,body{width:1200px;height:628px;overflow:hidden}
  body{
    font-family:"Outfit",sans-serif;
    background:linear-gradient(115deg,var(--navy-deep) 0%,#16195a 45%,var(--navy-light) 100%);
    position:relative;color:#fff;
  }
  .headline{
    position:absolute;left:24px;top:14px;width:1170px;
    font-size:40px;font-weight:400;line-height:50px;letter-spacing:-0.2px;
  }
  .headline .highlight{
    font-weight:700;
    background:linear-gradient(90deg,var(--teal),var(--brand-sky) 60%,var(--brand-mid));
    -webkit-background-clip:text;background-clip:text;color:transparent;
  }
  .section-band{
    position:absolute;left:19px;top:125px;width:1160px;height:32px;
    background:linear-gradient(90deg,#2a3f7e 0%,#25336e 60%,rgba(37,51,110,0) 100%);
    border-radius:4px;display:flex;align-items:center;
  }
  .section-band::before{
    content:"";width:18px;height:100%;border-radius:4px 0 0 4px;
    background:linear-gradient(180deg,var(--teal),var(--brand-mid));
  }
  .section-band h2{font-size:25px;font-weight:600;margin-left:18px}
  .card{
    position:absolute;left:19px;top:179px;width:1159px;height:426px;
    background:var(--card);border-radius:20px;
  }
  .card-notch{
    position:absolute;left:994px;top:549px;width:206px;height:79px;
    background:#263576;border-top-left-radius:22px;
  }
  .brand-tag{
    position:absolute;left:1006px;top:559px;width:172px;height:44px;
    background:#fff;border-radius:12px;
    display:flex;align-items:center;justify-content:center;gap:9px;
    color:var(--brand-blue);font-size:22px;font-weight:500;
  }
  .brand-tag .mark{width:22px;height:22px;background:var(--brand-mid);border-radius:4px}
  .note{position:absolute;top:188px;font-size:11px;letter-spacing:1.4px;color:var(--ink)}
  .note.today{left:142px}
  .note.future{left:934px}
  .table{
    position:absolute;left:36px;top:209px;width:1126px;
    display:grid;grid-template-columns:99px 306px 273px 220px 228px;
    color:var(--ink);
  }
  .head-blank{background:#fff;border-radius:10px 0 0 10px;height:51px}
  .head{
    height:51px;display:flex;align-items:center;gap:10px;padding-left:12px;
    font-weight:800;font-size:18px;line-height:18px;color:#fff;
    background:var(--navy-deep);
  }
  .head.b{background:linear-gradient(90deg,#121544,#1b2363)}
  .head.c{background:linear-gradient(90deg,#151a4f,#1f2868)}
  .head.d{background:linear-gradient(90deg,#1f2868,#2b3a86);border-radius:0 10px 10px 0}
  .head + .head{border-left:1px solid #2b3474}
  .badge{
    width:34px;height:34px;flex:none;display:grid;place-items:center;
    background:linear-gradient(135deg,var(--teal),var(--brand-mid));
    font-size:26px;font-weight:800;color:#fff;
  }
  .label{font-size:17px;padding-top:17px}
  .cell{border-left:1px solid var(--rule);padding:16px 6px 0 10px;font-size:16px;line-height:22px}
  .row-desc{height:90px}
  .row-ex{height:53px;border-top:1px solid var(--rule);display:flex;align-items:center;gap:16px;padding-top:0}
  .row-pro{height:83px;border-top:1px solid var(--rule);font-size:15px;padding-top:10px}
  .row-con{height:104px;border-top:1px solid var(--rule);font-size:15px;padding-top:12px}
  .label.ex{border-top:1px solid var(--rule);margin-left:15px;padding-top:8px;padding-left:0;margin-left:0}
  .label.ex,.label.pro,.label.con{border-top:1px solid var(--rule)}
  .label.ex{background:linear-gradient(90deg,var(--card) 15px,transparent 15px)}
  .label.pro{padding-top:10px}
  .label.con{padding-top:10px}
  .product{display:flex;align-items:center;gap:6px;font-size:17px;font-weight:600;color:var(--ink)}
  .product .dot{width:18px;height:18px;border-radius:50%;background:var(--brand-mid)}
  .aside{font-style:italic;font-size:13px}
  .pros,.cons{list-style:none}
  .pros li,.cons li{position:relative;padding-left:12px}
  .pros li::before{
    content:"";position:absolute;left:0;top:7px;width:7px;height:7px;
    border:1.5px solid var(--pro);border-radius:50%;
  }
  .cons li::before{
    content:"";position:absolute;left:0;top:6px;width:8px;height:8px;
    background:var(--con);border-radius:50%;
  }
  .inline-list{line-height:22px}
  .inline-list .pt{position:relative;padding-left:11px}
  .inline-list .pt::before{
    content:"";position:absolute;left:0;top:5px;width:7px;height:7px;
    border:1.8px solid var(--pro);border-radius:50%;
  }
  .inline-list .ct::before{border:none;background:var(--con);width:8px;height:8px}
</style>
</head>
<body>
  <h1 class="headline">There are <span class="highlight">3 MAJOR MONETIZATION MODELS</span> that have begun to gain traction with AI, and one we expect to see more of.</h1>

  <div class="section-band"><h2>Challenges of GenAI Monetization</h2></div>

  <div class="card"></div>
  <span class="note today">*FREQUENTLY SEEN TODAY</span>
  <span class="note future">*FUTURE OPTION?</span>

  <div class="table">
    <div class="head-blank"></div>
    <div class="head a"><span class="badge">A</span>User licenses</div>
    <div class="head b"><span class="badge">B</span>Usage-based<br>tokens</div>
    <div class="head c"><span class="badge">C</span>Outcome-based</div>
    <div class="head d"><span class="badge">D</span>Usage-tiered<br>licenses</div>

    <div class="label">Description</div>
    <div class="cell row-desc">Charge a flat price for a user to have access to the functionality</div>
    <div class="cell row-desc">Purchase blocks of tokens that can be spend on usage/work of the AI functionality</div>
    <div class="cell row-desc">Pay for the outcomes of the GenAI functionality</div>
    <div class="cell row-desc">Offer different user licenses with different usage capacities</div>

    <div class="label ex">Examples</div>
    <div class="cell row-ex">
      <span class="product"><span class="dot"></span>Chatterly</span>
      <span class="product"><span class="dot"></span>Wingmate</span>
    </div>
    <div class="cell row-ex">
      <span class="product"><span class="dot"></span>Neuronix</span>
      <span class="product" style="font-size:13px">Optiview API</span>
    </div>
    <div class="cell row-ex">
      <span class="product" style="font-size:15px">Supportly</span>
      <span class="product" style="font-size:15px"><span class="dot" style="width:14px;height:14px"></span>Refundr</span>
    </div>
    <div class="cell row-ex">
      <span class="product"><span class="dot"></span>Chatterly</span>
      <span class="aside">kinda...</span>
    </div>

    <div class="label pro">Pros</div>
    <div class="cell row-pro"><ul class="pros"><li style="font-size:16px">Simple and easily understood</li></ul></div>
    <div class="cell row-pro"><ul class="pros"><li style="font-size:14px">Covers costs at all scales of usage Tokens help with predictability issues</li></ul></div>
    <div class="cell row-pro"><ul class="pros"><li style="font-size:17px;line-height:22px">Potentially highly value-aligned</li></ul></div>
    <div class="cell row-pro"><p class="inline-list" style="font-size:14px"><span class="pt">Value aligned</span> <span class="pt">Simple &amp; predictable</span> <span class="pt">Natural upsell path</span> <span class="pt">Low barrier to adoption</span></p></div>

    <div class="label con">Cons</div>
    <div class="cell row-con"><p class="inline-list" style="font-size:15px"><span class="pt ct">High price limits adoption</span> <span class="pt ct">Not tightly value aligned</span> <span class="pt ct">Risky if fair usage restriction is not placed on</span> <span class="pt ct">Upsell dependent on wider adoption</span></p></div>
    <div class="cell row-con"><ul class="cons"><li>Not tightly value aligned (value may not increase linearly with usage)</li><li>Not ARR</li></ul></div>
    <div class="cell row-con"><ul class="cons"><li>Delayed revenue realization</li><li>Not ARR</li><li>Tough to find the right metric</li></ul></div>
    <div class="cell row-con"><ul class="cons"><li>Limit on the number of tiers</li></ul></div>
  </div>

  <div class="card-notch"></div>
  <div class="brand-tag"><span class="mark"></span>Strelquin</div>
</body>
</html>
```